Clockharbour Homepage Banner 1060 W x 100 H

Please see the attached 'word' document (Also copied below)
Feel free to use any images or logos from our website.
www.clockharbour.com.au

Background:
We are an Australian based official watch distributor/online retailer of international watch brands.

We require a new banner ad (1060 W x 100 H) to replace the existing one on our homepage www.clockharbour.com.au & wish to convey the following information:
*(Please feel free to alter wording, include or exclude points below & generally take creative license (with commercial reality in mind). We sell some luxury watches, so it must look professional & maintain a luxury look & feel.)

Clockharbour Direct:
Revolutionising the retail watch market !

- Buy direct from the official distributor & get world competitive
online prices (with full international warranty, & all original
papers, box & invoice)

- Eliminate all risk of fakes & non-existent factory warranty from
'grey' market sellers

- Free worldwide delivery over A$300

- Order online & 'try-on' in the comfort of your own home.
If you're not 100% happy, just post it back for a full refund or
exchange within 30 days

- Prefer to see & try on before purchase? Visit one of our retail
partner stores.

*** Feel free to copy any images from our website
www.clockharbour.com.au
Updates

Target Market(s)

Luxury watches

Industry/Entity Type

Retail

Font styles to use
Sans Serif

Requirements
Must have
• Visual imagery, text
Nice to have
• Feel free to use your creativity...
Should not have
• Cheap looking or tacky images. We sell some luxury watches, so we need to keep a professional & luxury image.

```html
<!DOCTYPE html>
<html lang="en">
<head>
<meta charset="utf-8">
<title>Clockharbour Homepage Banner Options</title>
<link href="https://fonts.googleapis.com/css2?family=Pathway+Gothic+One&display=swap" rel="stylesheet">
<style>
  :root {
    --page-bg: #e0e0e0;
    --banner-bg: #2a2a2a;
    --text-light: #e6e6e6;
    --accent-green: #3cb54a;
    --accent-orange: #d98a4a;
    --accent-blue: #2a9fd6;
  }
  html, body {
    margin: 0;
    padding: 0;
    overflow: hidden;
  }
  body {
    width: 1200px;
    height: 1200px;
    background: var(--page-bg);
    position: relative;
    font-family: "Pathway Gothic One", "Arial Narrow", sans-serif;
  }
  .banner {
    position: absolute;
    left: 30px;
    width: 1141px;
    height: 108px;
    background: var(--banner-bg);
    overflow: hidden;
  }
  .banner--green { top: 338px; }
  .banner--orange { top: 548px; }
  .banner--blue { top: 757px; }
  .banner--green .hl { color: var(--accent-green); }
  .banner--orange .hl { color: var(--accent-orange); }
  .banner--blue .hl { color: var(--accent-blue); }

  .watch-photo {
    position: absolute;
    top: 0;
    height: 108px;
  }
  .watch-photo--left {
    left: 0;
    width: 228px;
    background: radial-gradient(circle at 95px 50px, #1c1c1c 0 95px, #8a8a8a 96px 112px, #3a3a3a 113px, var(--banner-bg) 125px);
  }
  .watch-photo--right {
    right: 0;
    width: 257px;
    background: radial-gradient(circle at 160px 60px, #5a5a5a 0 100px, #b8b8b8 101px 112px, #1e1e1e 113px 125px, var(--banner-bg) 130px);
  }

  .message {
    position: absolute;
    left: 250px;
    width: 650px;
    top: 0;
    height: 108px;
    color: var(--text-light);
  }
  .message__line {
    position: absolute;
    left: 0;
    right: 0;
    margin: 0;
    text-align: center;
    white-space: nowrap;
    font-size: 20px;
    line-height: 30px;
    height: 30px;
  }
  .message__line--risk { top: 16px; }
  .message__line--direct { top: 66px; }
  .hl {
    font-size: 29px;
  }
</style>
</head>
<body>

<section class="banner banner--green">
  <div class="watch-photo watch-photo--left" role="img" aria-label="Black pilot automatic watch with orange seconds hand"></div>
  <div class="message">
    <p class="message__line message__line--risk"><span class="hl">Eliminate all Risk</span>&nbsp; of fakes &amp; <span class="hl">non-existent</span> factory warranty from <span class="hl">'grey'</span> market sellers</p>
    <p class="message__line message__line--direct">Buy <span class="hl">Direct</span> from the <span class="hl">Official Distributor</span> &amp; get world <span class="hl">Competitive</span> online <span class="hl">Prices</span></p>
  </div>
  <div class="watch-photo watch-photo--right" role="img" aria-label="Grey-dial automatic dress watch in steel case"></div>
</section>

<section class="banner banner--orange">
  <div class="watch-photo watch-photo--left" role="img" aria-label="Black pilot automatic watch with orange seconds hand"></div>
  <div class="message">
    <p class="message__line message__line--risk"><span class="hl">Eliminate all Risk</span>&nbsp; of fakes &amp; <span class="hl">non-existent</span> factory warranty from <span class="hl">'grey'</span> market sellers</p>
    <p class="message__line message__line--direct">Buy <span class="hl">Direct</span> from the <span class="hl">Official Distributor</span> &amp; get world <span class="hl">Competitive</span> online <span class="hl">Prices</span></p>
  </div>
  <div class="watch-photo watch-photo--right" role="img" aria-label="Grey-dial automatic dress watch in steel case"></div>
</section>

<section class="banner banner--blue">
  <div class="watch-photo watch-photo--left" role="img" aria-label="Black pilot automatic watch with orange seconds hand"></div>
  <div class="message">
    <p class="message__line message__line--risk"><span class="hl">Eliminate all Risk</span>&nbsp; of fakes &amp; <span class="hl">non-existent</span> factory warranty from <span class="hl">'grey'</span> market sellers</p>
    <p class="message__line message__line--direct">Buy <span class="hl">Direct</span> from the <span class="hl">Official Distributor</span> &amp; get world <span class="hl">Competitive</span> online <span class="hl">Prices</span></p>
  </div>
  <div class="watch-photo watch-photo--right" role="img" aria-label="Grey-dial automatic dress watch in steel case"></div>
</section>

</body>
</html>
```